you will use Ai to Copy the website Quellabyx.com to come up with the basic frame work and it will give you the understanding of how I would like Zandoprik.com to be like. Zandoprik.com is a peer to peer rv rental site very similar to both of the other rv rental sites the difference is that are commission based 20% and above per rental and we will be one flat monthly rate and they keep all the earnings. Below is photo that will help you with the color scheme and the look and feel of the design

```html
<!DOCTYPE html>
<html lang="en">
<head>
<meta charset="utf-8">
<title>Zandoprik.com — Rent &amp; Own RVs</title>
<link href="https://fonts.googleapis.com/css2?family=Lexend:wght@400;500;600&family=Lato:wght@400;700&display=swap" rel="stylesheet">
<style>
:root{
  --green:#6a9e2b;
  --green-dark:#5a8c1f;
  --green-light:#8bc34a;
  --navy:#1b2a50;
  --ink:#222;
  --muted:#444;
  --line:#cfcfcf;
  --white:#fff;
  --mint:#eef3e2;
}
*{box-sizing:border-box;margin:0;padding:0}
html,body{width:1200px;height:3893px;overflow:hidden}
body{font-family:"Lato",sans-serif;color:var(--ink);background:var(--white);position:relative}
.abs{position:absolute}
h1,h2,h3,.logo,.nav-links,.btn{font-family:"Lexend",sans-serif}
.btn{position:absolute;display:flex;align-items:center;justify-content:center;border-radius:23px;color:#fff;font-weight:500;font-size:17px;background:linear-gradient(180deg,var(--green-light),var(--green-dark));box-shadow:0 2px 4px rgba(0,0,0,.2)}
/* header */
.site-header{top:0;left:0;width:1200px;height:86px;background:#fff}
.logo{font-size:29px;font-weight:500;color:var(--green)}
.site-header .logo{left:109px;top:24px}
.nav-links{left:387px;top:32px;display:flex;gap:35px;font-size:15px;color:#333}
/* hero */
.hero{top:86px;left:0;width:1200px;height:599px;background:linear-gradient(180deg,#7a3a28 0%,#c4552a 35%,#d9822e 55%,#3a2a2e 80%,#1f1e28 100%)}
.hero h1{position:absolute;left:109px;top:78px;font-size:53px;font-weight:500;line-height:64px;color:#fff}
.hero .tagline{position:absolute;left:109px;top:224px;font-family:"Lexend",sans-serif;font-size:18px;font-weight:500;color:#fff}
.hero .intro{position:absolute;left:109px;top:268px;width:510px;font-size:15px;font-weight:700;line-height:26px;color:#fff}
.search{left:110px;top:544px;width:978px;height:106px;background:#fff;border-radius:6px;box-shadow:0 2px 8px rgba(0,0,0,.2)}
.field{position:absolute;top:28px}
.field label{display:flex;align-items:center;gap:8px;font-size:14.5px;color:#333}
.field .box{margin-top:8px;height:32px;border:1.5px solid var(--line);border-radius:3px;font-size:13px;color:#333;padding:0 14px;display:flex;align-items:center;justify-content:space-between}
/* sections */
h2{position:absolute;width:1200px;text-align:center;font-weight:500;font-size:40px;color:var(--green)}
.center-p{position:absolute;left:130px;width:940px;text-align:center;font-size:15px;line-height:26px;color:var(--muted)}
.why{top:685px;left:0;width:1200px;height:486px;background:#fff}
.why .sub{position:absolute;top:146px;width:1200px;text-align:center;font-family:"Lexend",sans-serif;font-size:21px;color:var(--ink)}
.why strong{color:var(--green-dark);font-weight:700}
.types{top:1171px;left:0;width:1200px;height:642px;background:linear-gradient(180deg,#dde6c6,#eef2e2 40%,#e9efdb)}
.card{position:absolute;top:189px;width:311px;height:367px;background:#fff;border-radius:6px;box-shadow:0 1px 5px rgba(0,0,0,.25);overflow:hidden}
.card .ph{height:211px}
.card h3{position:absolute;left:25px;top:224px;font-size:16px;font-weight:500}
.card p{position:absolute;left:25px;top:250px;width:265px;font-size:13.5px;line-height:25.5px;color:var(--muted)}
.card .more{position:absolute;left:27px;top:332px;font-size:14px;font-style:italic;text-decoration:underline;color:#333}
.card svg.go{position:absolute;right:20px;top:334px}
.arrow-btn{position:absolute;top:352px}
.diff{top:1813px;left:0;width:1200px;height:620px}
.diff .ph{position:absolute;left:53px;top:182px;width:544px;height:347px;border-radius:40px;background:radial-gradient(ellipse at center,#c9bfae 0%,#e8e2d6 55%,#fff 75%)}
.diff .lead{position:absolute;left:641px;top:147px;width:447px;font-size:14.5px;line-height:26px;color:var(--muted);text-align:justify}
.diff h3{position:absolute;left:640px;top:262px;font-size:22px;font-weight:500;color:var(--green)}
.benefits{position:absolute;left:643px;top:305px;list-style:none}
.benefits li{display:flex;align-items:center;gap:14px;height:38.5px;font-size:17px;color:#333}
.pricing{top:2433px;left:0;width:1200px;height:364px;background:linear-gradient(180deg,#2a3557,#1b2a50)}
.pricing h2{color:#fff;top:76px;font-size:42px}
.pricing p{position:absolute;left:160px;width:880px;top:153px;text-align:center;color:#fff;font-size:15px;line-height:26px}
.dest{top:2797px;left:0;width:1200px;height:675px}
.dest .sub{position:absolute;width:1200px;text-align:center;top:143px;font-size:15px;line-height:26px;color:#333}
.place{position:absolute;top:220px;width:234px}
.place .ph{height:256px;border-radius:6px;box-shadow:0 1px 4px rgba(0,0,0,.3)}
.place span{display:block;text-align:center;margin-top:16px;font-size:15px;font-weight:700;color:#222}
.footer{top:3472px;left:0;width:1200px;height:421px;background:var(--navy);color:#fff}
.footer .logo{position:absolute;left:108px;top:95px;color:#fff;font-size:30px}
.subscribe{position:absolute;left:110px;top:168px;width:260px;height:42px;background:#fff;border-radius:3px;font-size:14px;color:#444;padding:0 14px;display:flex;align-items:center}
.subscribe .send{position:absolute;right:0;top:0;width:46px;height:42px;background:var(--green-light);border-radius:0 3px 3px 0;display:flex;align-items:center;justify-content:center}
.fcol{position:absolute;top:92px}
.fcol h4{font-family:"Lexend",sans-serif;font-weight:400;font-size:19px;margin-bottom:14px}
.fcol ul{list-style:none}
.fcol li{height:34.5px;font-size:14px;display:flex;align-items:flex-start;gap:14px}
.fcol li::before{content:"";width:7px;height:7px;border-radius:50%;background:#fff;margin-top:5px;margin-left:3px}
.fcol.contact li::before{display:none}
.fcol.contact li{gap:10px;height:45px}
.rule{position:absolute;left:108px;top:368px;width:980px;height:1px;background:#5a6585}
.social{position:absolute;left:109px;top:380px;display:flex;gap:10px}
.social span{width:21px;height:21px;border-radius:50%;border:2px solid #fff}
.copy{position:absolute;top:384px;width:1200px;text-align:center;font-size:14px}
</style>
</head>
<body>

<header class="abs site-header">
  <div class="abs logo">Zandoprik.com</div>
  <nav class="abs nav-links"><span>Home</span><span>Browse RVs</span><span>List Your RV</span><span>How It Works</span><span>Membership</span></nav>
  <div class="btn" style="left:950px;top:18px;width:138px;height:47px">Contact Us</div>
</header>

<section class="abs hero" role="img" aria-label="Class C motorhome parked by a lake at sunset">
  <h1>The Smarter Way to<br>Rent &amp; Own RVs</h1>
  <div class="tagline">Keep 100% of Every Rental. Pay One Simple Monthly Fee.</div>
  <p class="intro">Whether you're planning your next road trip or turning your RV into a profitable business, Zandoprik connects travelers directly with RV owners—without costly commission fees.</p>
  <div class="btn" style="left:109px;top:367px;width:137px;height:45px">Browse RVs</div>
  <div class="btn" style="left:258px;top:367px;width:138px;height:45px">List Your RV</div>
</section>

<form class="abs search">
  <div class="field" style="left:22px;width:240px">
    <label><svg width="14" height="17" viewBox="0 0 14 17"><path d="M7 0a7 7 0 0 0-7 7c0 5 7 10 7 10s7-5 7-10a7 7 0 0 0-7-7z" fill="#1b2a50"/><circle cx="7" cy="7" r="2.6" fill="#fff"/></svg>Where are you going?</label>
    <div class="box">Enter destination or location <svg width="14" height="8"><path d="M0 0h14L7 8z" fill="#444"/></svg></div>
  </div>
  <div class="field" style="left:289px;width:146px">
    <label><svg width="16" height="16"><rect x="1" y="2" width="14" height="13" fill="#1b2a50"/><rect x="3" y="6" width="10" height="7" fill="#fff"/><rect x="4" y="7" width="2" height="2" fill="#1b2a50"/><rect x="7" y="7" width="2" height="2" fill="#1b2a50"/><rect x="10" y="7" width="2" height="2" fill="#1b2a50"/></svg>Pick-up Date</label>
    <div class="box">Select date <svg width="14" height="8"><path d="M0 0h14L7 8z" fill="#444"/></svg></div>
  </div>
  <div class="field" style="left:461px;width:146px">
    <label><svg width="16" height="16"><rect x="1" y="2" width="14" height="13" fill="#1b2a50"/><rect x="3" y="6" width="10" height="7" fill="#fff"/><rect x="4" y="7" width="2" height="2" fill="#1b2a50"/><rect x="7" y="7" width="2" height="2" fill="#1b2a50"/><rect x="10" y="7" width="2" height="2" fill="#1b2a50"/></svg>Return Date</label>
    <div class="box">Select date <svg width="14" height="8"><path d="M0 0h14L7 8z" fill="#444"/></svg></div>
  </div>
  <div class="field" style="left:630px;width:146px">
    <label><svg width="26" height="14"><rect x="0" y="2" width="18" height="9" rx="1" fill="#1b2a50"/><path d="M18 4h5l3 4v3h-8z" fill="#1b2a50"/><circle cx="5" cy="12" r="2" fill="#1b2a50"/><circle cx="21" cy="12" r="2" fill="#1b2a50"/></svg>RV Type</label>
    <div class="box">All RV Types <svg width="14" height="8"><path d="M0 0h14L7 8z" fill="#444"/></svg></div>
  </div>
  <div class="btn" style="left:806px;top:29px;width:138px;height:46px">Search RVs</div>
</form>

<section class="abs why">
  <h2 style="top:78px">Why Choose Zandoprik</h2>
  <div class="sub">More Freedom. More Earnings. Zero Commission</div>
  <p class="center-p" style="top:195px">Zandoprik is changing the way people rent and own RVs. Unlike traditional rental marketplaces that take a percentage of every booking, we offer a simple monthly membership that lets owners keep every dollar they earn. Whether you're renting out your RV a few weekends each year or managing multiple vehicles, you'll enjoy predictable costs, complete control, and unlimited earning potential.</p>
  <p class="center-p" style="top:282px">Unlike other RV rental marketplaces that take <strong>20% or more from every booking</strong>, Zandoprik lets owners pay one affordable monthly subscription and keep <strong>100% of every rental dollar they earn</strong>.</p>
  <div class="btn" style="left:530px;top:353px;width:136px;height:45px">Read More</div>
</section>

<section class="abs types">
  <h2 style="top:75px">Find the Perfect RV for Every Journey</h2>
  <p class="center-p" style="top:141px">From luxury motorhomes to adventure-ready toy haulers, explore a wide range of RVs that fit your travel style, needs, and budget.</p>
  <svg class="arrow-btn" style="left:35px" width="42" height="42" viewBox="0 0 42 42"><circle cx="21" cy="21" r="19" fill="none" stroke="#555" stroke-width="2"/><path d="M29 21H13m6-6-6 6 6 6" fill="none" stroke="#555" stroke-width="2"/></svg>
  <svg class="arrow-btn" style="left:1121px" width="42" height="42" viewBox="0 0 42 42"><circle cx="21" cy="21" r="19" fill="none" stroke="#1b2a50" stroke-width="2"/><path d="M13 21h16m-6-6 6 6-6 6" fill="none" stroke="#1b2a50" stroke-width="2"/></svg>
  <article class="card" style="left:109px">
    <div class="ph" role="img" aria-label="Class A motorhome beside a mountain lake" style="background:linear-gradient(180deg,#c9a064,#8a8f86 60%,#4f5d4a)"></div>
    <h3>Class A Motorhomes</h3>
    <p>Experience luxury on the road with spacious interiors, premium amenities, and first-class comfort.</p>
    <span class="more">Read More</span>
    <svg class="go" width="18" height="14"><path d="M0 7h16m-6-6 6 6-6 6" fill="none" stroke="#444" stroke-width="2"/></svg>
  </article>
  <article class="card" style="left:444px">
    <div class="ph" role="img" aria-label="Class B camper van on a mountain road" style="background:linear-gradient(180deg,#8fa8c8,#b9bcc0 50%,#5a5f5c)"></div>
    <h3>Class B Camper Vans</h3>
    <p>Compact, fuel-efficient, and perfect for weekend adventures or solo travel.</p>
    <span class="more">Read More</span>
    <svg class="go" width="18" height="14"><path d="M0 7h16m-6-6 6 6-6 6" fill="none" stroke="#444" stroke-width="2"/></svg>
  </article>
  <article class="card" style="left:778px">
    <div class="ph" role="img" aria-label="Class C motorhome parked by a lake" style="background:linear-gradient(180deg,#9fb6cf,#d6d2c4 55%,#8d8a6c)"></div>
    <h3>Class C Motorhomes</h3>
    <p>Family-friendly RVs offering comfort, convenience, and plenty of room for memorable road trips.</p>
    <span class="more">Read More</span>
    <svg class="go" width="18" height="14"><path d="M0 7h16m-6-6 6 6-6 6" fill="none" stroke="#444" stroke-width="2"/></svg>
  </article>
</section>

<section class="abs diff">
  <h2 style="top:75px">Why Zandoprik is Different</h2>
  <div class="ph" role="img" aria-label="Cream Class C motorhome"></div>
  <p class="lead">Every booking should increase your profits—not your fees With Zandoprik, you pay one affordable monthly subscription instead of losing 20% or more on every reservation. The more bookings you receive, the more money you keep.</p>
  <h3>Benefits</h3>
  <ul class="benefits">
    <li><svg width="17" height="17"><circle cx="8.5" cy="8.5" r="8.5" fill="#1b2a50"/><path d="M4 8.5h8m-3-3 3 3-3 3" fill="none" stroke="#fff" stroke-width="1.6"/></svg>Flat Monthly Membership</li>
    <li><svg width="17" height="17"><circle cx="8.5" cy="8.5" r="8.5" fill="#1b2a50"/><path d="M4 8.5h8m-3-3 3 3-3 3" fill="none" stroke="#fff" stroke-width="1.6"/></svg>Keep 100% of Rental Income</li>
    <li><svg width="17" height="17"><circle cx="8.5" cy="8.5" r="8.5" fill="#1b2a50"/><path d="M4 8.5h8m-3-3 3 3-3 3" fill="none" stroke="#fff" stroke-width="1.6"/></svg>Unlimited Bookings</li>
    <li><svg width="17" height="17"><circle cx="8.5" cy="8.5" r="8.5" fill="#1b2a50"/><path d="M4 8.5h8m-3-3 3 3-3 3" fill="none" stroke="#fff" stroke-width="1.6"/></svg>No Hidden Fees</li>
    <li><svg width="17" height="17"><circle cx="8.5" cy="8.5" r="8.5" fill="#1b2a50"/><path d="M4 8.5h8m-3-3 3 3-3 3" fill="none" stroke="#fff" stroke-width="1.6"/></svg>Full Pricing Control</li>
    <li><svg width="17" height="17"><circle cx="8.5" cy="8.5" r="8.5" fill="#1b2a50"/><path d="M4 8.5h8m-3-3 3 3-3 3" fill="none" stroke="#fff" stroke-width="1.6"/></svg>Professional Booking Tools</li>
  </ul>
</section>

<section class="abs pricing" role="img" aria-label="Faded RV at a campsite behind a navy overlay">
  <h2>Simple Pricing. Maximum Earnings.</h2>
  <p>Choose the membership plan that fits your rental goals. Whether you own one RV or an entire fleet, our subscription plans are designed to help you maximize your income without worrying about commission fees.</p>
  <div class="btn" style="left:474px;top:232px;width:247px;height:46px">View Membership Plans</div>
</section>

<section class="abs dest">
  <h2 style="top:77px">Popular Destinations</h2>
  <p class="sub">Discover Your Next Road Trip<br>Start your adventure by exploring some of North America's most iconic travel destinations.</p>
  <div class="place" style="left:110px"><div class="ph" role="img" aria-label="Waterfall in a yellow canyon" style="background:linear-gradient(180deg,#7aa0c8,#6f8a4a 35%,#b58f4e 70%,#6d7a48)"></div><span>Yellowstone National Park</span></div>
  <div class="place" style="left:358px"><div class="ph" role="img" aria-label="Granite dome at dusk" style="background:linear-gradient(180deg,#e08a6a,#a0706a 35%,#4f5a6a 70%,#2b3440)"></div><span>Yosemite National Park</span></div>
  <div class="place" style="left:607px"><div class="ph" role="img" aria-label="Alpine lake with pine trees and mountains" style="background:linear-gradient(180deg,#9fc0e0,#4c6e4a 40%,#7aa6b2 65%,#5e6f6a)"></div><span>Glacier National Park</span></div>
  <div class="place" style="left:855px"><div class="ph" role="img" aria-label="Red canyon cliffs above a river at sunset" style="background:linear-gradient(180deg,#e5a077,#b9573a 35%,#7d6a38 65%,#6a4a32)"></div><span>Zion National Park</span></div>
  <div class="btn" style="left:530px;top:544px;width:136px;height:45px">View More</div>
</section>

<footer class="abs footer">
  <div class="logo">Zandoprik.com</div>
  <div class="subscribe">Enter email address<span class="send"><svg width="20" height="20" viewBox="0 0 20 20"><path d="M19 1 1 8l7 3 3 7z" fill="#fff"/></svg></span></div>
  <div class="fcol" style="left:438px"><h4>Quick Links</h4><ul><li>Home</li><li>Browse RVs</li><li>RV Categories</li><li>Popular Destinations</li><li>Road Trip Inspiration</li><li>Travel Guides</li><li>Blog</li></ul></div>
  <div class="fcol" style="left:654px"><h4>For RV Owners</h4><ul><li>List Your RV</li><li>Membership Plans</li><li>Why Choose Zandoprik</li><li>Owner Dashboard</li><li>Owner Resources</li><li>Pricing Calculator</li><li>Success Stories</li></ul></div>
  <div class="fcol contact" style="left:902px"><h4>Contact Us</h4><ul>
    <li><svg width="16" height="16"><circle cx="8" cy="8" r="8" fill="#fff"/><circle cx="8" cy="7" r="2.5" fill="#1b2a50"/></svg>Zandoprik</li>
    <li><svg width="16" height="16"><circle cx="8" cy="8" r="8" fill="#fff"/><rect x="4" y="5" width="8" height="6" fill="#1b2a50"/></svg>support@zandoprik.com</li>
    <li><svg width="16" height="16"><circle cx="8" cy="8" r="8" fill="#fff"/><path d="M5 4l2 2-1 1.5 2.5 2.5L10 9l2 2-1.5 1.5C7 12 4 9 3.5 5.5z" fill="#1b2a50"/></svg>(800) 555-0142</li>
  </ul></div>
  <div class="rule"></div>
  <div class="social"><span></span><span></span><span></span><span></span></div>
  <div class="copy">© 2026 Zandoprik. All Rights Reserved</div>
</footer>

</body>
</html>
```